Letterhead Design Project

Please see attached logo as well as information below which could be relevant to design. Let me know if you have any questions.

Derek J. Holloman
Estate Planning and Insurance Specialist
Dholloman@brenwickfinancial.com
P: 516-471-2958 F: 516-471-3085
www.brenwickfinancial.com
4300 Maple Ridge Road, Suite 305E
Syosset, New York 11804

```html
<!DOCTYPE html>
<html lang="en">
<head>
<meta charset="utf-8">
<title>Brenwick Financial Group Letterhead</title>
<link rel="stylesheet" href="https://fonts.googleapis.com/css2?family=Montserrat:wght@400;500;600&display=swap">
<style>
  :root {
    --ink: #2b2d38;
    --ink-deep: #1f2029;
    --gold: #c9a24a;
    --paper: #ffffff;
    --text: #3a3a3a;
    --faint: #f3efe4;
    --faint-line: #ebe4d2;
  }
  * { margin: 0; padding: 0; box-sizing: border-box; }
  html, body { width: 851px; height: 1200px; overflow: hidden; background: var(--paper); }
  body { font-family: "Montserrat", Arial, sans-serif; color: var(--text); }
  .letterhead { position: relative; width: 851px; height: 1200px; background: var(--paper); }

  .top-band {
    position: absolute; left: 0; top: 51px; width: 851px; height: 86px;
    background: var(--ink);
  }
  .brand-tab {
    position: absolute; left: 34px; top: 51px; width: 292px; height: 104px;
    background: var(--ink-deep); border-radius: 0 0 10px 10px;
    display: flex; align-items: center; gap: 12px; padding-left: 22px;
  }
  .brand-square { width: 40px; height: 40px; border: 2px solid var(--gold); flex: none; }
  .brand-name {
    font-size: 15px; font-weight: 500; letter-spacing: 1.5px; color: var(--paper);
    text-transform: uppercase; line-height: 1.25;
  }

  .signatory {
    position: absolute; right: 34px; top: 62px; text-align: right;
  }
  .signatory-name { font-size: 15px; font-weight: 600; color: var(--gold); }
  .signatory-title { font-size: 11px; font-weight: 400; color: var(--paper); margin-top: 3px; }

  .watermark {
    position: absolute; left: 305px; top: 510px; width: 240px; height: 240px;
    border: 3px solid var(--faint-line); background: var(--faint);
    display: flex; align-items: center; justify-content: center;
  }
  .watermark-name {
    font-size: 24px; font-weight: 500; letter-spacing: 4px; color: var(--faint-line);
    text-transform: uppercase;
  }

  .contact {
    position: absolute; left: 28px; top: 1100px; font-size: 12px; line-height: 16px;
  }
  .contact-row { display: flex; }
  .contact-label { color: var(--gold); width: 72px; font-weight: 500; }
  .contact-value { color: var(--text); }

  .bottom-band {
    position: absolute; left: 0; top: 1158px; width: 851px; height: 28px;
    background: var(--ink);
    display: flex; align-items: center; justify-content: flex-end; padding-right: 34px;
    font-size: 11px; color: var(--paper);
  }
  .office-label { color: var(--gold); font-weight: 600; margin-right: 6px; }
</style>
</head>
<body>
<div class="letterhead">
  <div class="top-band"></div>
  <div class="brand-tab">
    <div class="brand-square"></div>
    <div class="brand-name">Brenwick<br>Financial Group</div>
  </div>
  <div class="signatory">
    <div class="signatory-name">Derek J. Holloman</div>
    <div class="signatory-title">Estate Planning and Insurance Specialist</div>
  </div>

  <div class="watermark"><span class="watermark-name">Brenwick</span></div>

  <div class="contact">
    <div class="contact-row"><span class="contact-label">E-mail:</span><span class="contact-value">Dholloman@brenwickfinancial.com</span></div>
    <div class="contact-row"><span class="contact-label">Phone :</span><span class="contact-value">516-471-2958 F: 516-471-3085</span></div>
    <div class="contact-row"><span class="contact-label">Website:</span><span class="contact-value">www.brenwickfinancial.com</span></div>
  </div>

  <div class="bottom-band">
    <span class="office-label">Head Office :</span>
    <span>4300 Maple Ridge Road, Suite 305E Syosset, New York 11804</span>
  </div>
</div>
</body>
</html>
```